Create Web Design Template with Source Files

I need a web design built with PSD/source files. See attached design I have made to guidance. Also I have attached an image I have used so you can use it.

I got my inspiration from this site if you would like to use it also:
http://trelvix.com/home

PSD & html slicing and responsive designs also. So we can run across all devices.

Number of Pages Required

1 page

Requirements
Must have
• See attachments. Ask if you have any questions...

```html
<!DOCTYPE html>
<html lang="en">
<head>
<meta charset="utf-8">
<title>Lumo – Channel Feed</title>
<link href="https://fonts.googleapis.com/css2?family=Roboto:wght@400;500;700&family=Roboto+Slab:wght@500&display=swap" rel="stylesheet">
<style>
:root{
  --purple:#8512a8;
  --green:#3f9a3b;
  --ink:#1d1d1d;
  --muted:#8d8d8d;
  --side:#0d0d0d;
  --foot:#e1e1e1;
  --line:#ececec;
  --white:#ffffff;
}
*{box-sizing:border-box;margin:0;padding:0}
html,body{width:1200px;height:2192px;overflow:hidden}
body{position:relative;background:var(--white);font-family:"Roboto",Arial,sans-serif;color:var(--ink)}
ul{list-style:none}
.ic{width:1em;height:1em;fill:currentColor;vertical-align:-0.12em}

.screen{position:absolute;overflow:hidden;background:var(--white)}

/* ---------- shared bits ---------- */
.hero{position:absolute;background:
  radial-gradient(ellipse at 30% 30%,rgba(120,100,90,.45),transparent 60%),
  radial-gradient(ellipse at 75% 20%,rgba(90,80,80,.4),transparent 55%),
  linear-gradient(180deg,#3a3433 0%,#201c1c 55%,#0d0b0b 100%)}
.back{display:inline-flex;align-items:center;justify-content:center;border-radius:50%;background:var(--purple);color:var(--white)}
.brand{font-weight:700;color:var(--white);letter-spacing:.2px}
.brand.dark{color:var(--ink)}
.round{display:inline-flex;align-items:center;justify-content:center;border-radius:50%;background:var(--purple);color:var(--white)}
.btn{display:inline-flex;align-items:center;justify-content:center;gap:3px;font-weight:700;color:var(--white);background:var(--purple);border-radius:2px;text-transform:uppercase}
.btn.sub{background:var(--green)}
.thumb{position:relative;width:100%}
.len{position:absolute;right:3px;bottom:3px;background:rgba(0,0,0,.7);color:var(--white);border-radius:1px}
.t-pizza{background:linear-gradient(135deg,#6b2e14,#d5843a 40%,#c03a1d 65%,#f1dcb8)}
.t-meat{background:linear-gradient(160deg,#2e2116,#7e6246 45%,#d8cfbf 80%,#58402c)}
.t-steak{background:linear-gradient(150deg,#241812,#6b4632 50%,#a57656 80%,#3a271c)}
.t-pasta{background:linear-gradient(170deg,#4a2614,#c27637 45%,#e7bf7e 75%,#8a4a22)}
.t-sunset{background:linear-gradient(180deg,#f7c544,#ee8b2c 50%,#c45a22 75%,#4e3018)}
.t-friends{background:linear-gradient(120deg,#dfe3d8,#e6d3c1 45%,#9fae72 80%,#c9b8a6)}
.t-bikes{background:linear-gradient(160deg,#3e6a34,#8ab04c 45%,#2f4f6c 75%,#5f8d3d)}
.t-juice{background:linear-gradient(110deg,#eceae4,#cfd5d1 50%,#d8a35f 80%,#e8e2d8)}
.meta{display:flex;justify-content:space-between;align-items:center;color:var(--muted)}
.src{display:inline-flex;align-items:center;gap:3px}
.badge{display:inline-block;background:#b9b9b9;border-radius:50%}
.badge.sq{background:#111;border-radius:0}
.nav li{display:flex;align-items:center;gap:4px;color:var(--white)}
.nav li.on{background:var(--purple);border-radius:2px}
.load{display:flex;justify-content:center}

/* ---------- desktop ---------- */
.desk{top:41px;width:533px;height:725px}
#desk-overlay{left:52px}
#desk-bar{left:607px}
.desk .side{position:absolute;left:0;top:0;width:120px;bottom:0;background:linear-gradient(180deg,#141414,#070707)}
.desk .hero{left:120px;top:0;right:0;height:191px}
.desk .logo{position:absolute;left:20px;top:14px;display:flex;align-items:center;gap:6px}
.desk .back{width:13px;height:13px;font-size:8px}
.desk .brand{font-size:14px}
.desk .nav{position:absolute;left:9px;top:56px;width:103px}
.desk .nav li{height:17px;padding-left:8px;font-size:6px;margin-bottom:12px}
.desk .tools{position:absolute;top:13px;left:305px;display:flex;align-items:center;gap:8px}
.desk .search{width:130px;height:15px;border-bottom:1px solid rgba(255,255,255,.6);font-size:6px;color:#ddd;display:flex;align-items:center;padding-left:2px}
.desk .round{width:13px;height:13px;font-size:6px}
.desk .login{width:50px;height:15px;font-size:6px;margin-left:3px}
.desk .main{position:absolute;left:120px;top:191px;right:0;padding:0 14px}
.feed{border-bottom:1px solid var(--line)}
.desk .feed{height:241px;padding-top:20px}
.desk .feed+.feed{border-bottom:0;padding-top:24px}
.feed-head{display:flex;justify-content:space-between;align-items:center}
.desk h2{font-family:"Roboto Slab",Georgia,serif;font-weight:500;font-size:13px}
.desk .sub{width:55px;height:11px;font-size:5px}
.desk .intro{width:285px;margin-top:6px;font-size:5.2px;line-height:11px;color:var(--muted)}
.desk .grid{display:grid;grid-template-columns:repeat(4,1fr);gap:6px;margin-top:6px}
.desk .thumb{height:67px}
.desk .len{font-size:4.5px;padding:1px 3px}
.desk .card h3{font-size:6.4px;font-weight:500;line-height:9.5px;margin:4px 0 3px;height:19px}
.desk .meta{font-size:4.4px}
.desk .badge{width:8px;height:6px}
.desk .load{margin-top:10px}
.desk .load .btn{width:64px;height:17px;font-size:5.6px}
.desk .foot{position:absolute;left:120px;right:0;bottom:0;height:38px;background:var(--foot);display:flex;justify-content:space-between;align-items:center;padding:0 17px;font-size:5px;color:#555}
#desk-bar .topbar{position:absolute;left:0;top:0;right:0;height:36px;background:var(--white);border-bottom:1px solid var(--line);z-index:2}
#desk-bar .logo{left:20px;top:11px}
#desk-bar .tools{left:302px;top:10px}
#desk-bar .search{border-color:#bbb;color:#666}
#desk-bar .side{top:36px}
#desk-bar .hero{top:36px;height:155px}
#desk-bar .nav{top:21px}

/* ---------- mobile ---------- */
.mob{top:861px;width:159px;height:1231px}
#mob-a{left:186px}
#mob-a-menu{left:400px}
#mob-b{left:633px}
#mob-b-menu{left:846px}
.mob .hero{left:0;right:0;top:0;height:138px}
.mob .bar{position:absolute;left:0;right:0;top:0;height:36px;display:flex;align-items:center;justify-content:space-between;padding:0 12px}
.mob .brand{font-size:11px}
.mob .acts{display:flex;align-items:center;gap:6px;color:var(--purple)}
.mob .round{width:11px;height:11px;font-size:5.5px}
.mob .menu{font-size:10px}
.mob.lite .bar{height:32px;background:var(--white);border-bottom:1px solid var(--line)}
.mob.lite .hero{top:32px;height:106px}
.mob .main{position:absolute;left:0;right:0;top:138px;padding:0 23px}
.mob .feed{padding:20px 0 14px}
.mob .feed+.feed{border-bottom:0;padding-top:18px}
.mob h2{font-family:"Roboto Slab",Georgia,serif;font-weight:500;font-size:11px;line-height:13px;margin-bottom:4px}
.mob .card{width:113px;margin-bottom:16px}
.mob .thumb{height:65px}
.mob .len{font-size:4.5px;padding:1px 3px}
.mob .card h3{font-size:6.2px;font-weight:500;line-height:8.5px;margin:5px 0 4px}
.mob .meta{font-size:4.3px}
.mob .badge{width:7px;height:5px}
.mob .load .btn{width:58px;height:16px;font-size:5.2px}
.mob .foot{position:absolute;left:0;right:0;bottom:0;height:36px;background:var(--foot);text-align:center;font-size:4.4px;color:#555;line-height:8px;padding-top:9px}
.veil{position:absolute;inset:0;background:rgba(0,0,0,.9);z-index:3}
.drawer{position:absolute;right:0;top:0;width:105px;height:293px;background:#0b0b0b;z-index:4;padding:15px 10px 0 9px}
.drawer .nav li{height:14px;padding-left:6px;font-size:5px;margin-bottom:14px}
.close{position:absolute;left:14px;top:15px;z-index:4;color:var(--purple);font-size:11px}
</style>
</head>
<body>

<svg width="0" height="0" style="position:absolute" aria-hidden="true">
  <symbol id="i-home" viewBox="0 0 16 16"><path d="M8 1.5 1 8h2v6.5h3.8v-4h2.4v4H13V8h2z"/></symbol>
  <symbol id="i-help" viewBox="0 0 16 16"><path d="M5 5.5a3 3 0 1 1 4.4 2.6C8.5 8.6 8.3 9 8.3 10H7V9.6c0-1.4.6-2 1.6-2.6A1.6 1.6 0 1 0 6.4 5.5zM7 11.5h1.6v2H7z"/></symbol>
  <symbol id="i-user" viewBox="0 0 16 16"><circle cx="8" cy="4.6" r="3.2"/><path d="M1.8 15c0-3.6 2.8-6 6.2-6s6.2 2.4 6.2 6z"/></symbol>
  <symbol id="i-trophy" viewBox="0 0 16 16"><path d="M4 1.5h8v2h2.5c0 3-1.4 4.6-3.4 4.9A4 4 0 0 1 9 10.5V12h2.5v2.5h-7V12H7v-1.5a4 4 0 0 1-2.1-2.1C2.9 8.1 1.5 6.5 1.5 3.5H4zM2.9 5c.2 1.2.7 1.8 1.3 2.1L4 5zM13.1 5H12l-.2 2.1c.6-.3 1.1-.9 1.3-2.1z"/></symbol>
  <symbol id="i-chat" viewBox="0 0 16 16"><path d="M6.5 2C3.5 2 1 3.8 1 6c0 1.1.6 2.1 1.6 2.8L2 11l2.6-1.3c.6.2 1.2.3 1.9.3 3 0 5.5-1.8 5.5-4S9.5 2 6.5 2z"/><path d="M13.4 6.6c.1 2.6-2.6 4.6-5.8 4.8 1 .9 2.4 1.4 4 1.4.5 0 1-.1 1.4-.2L15 13.6l-.5-2c.9-.6 1.5-1.5 1.5-2.5 0-1-.6-1.9-1.6-2.5z"/></symbol>
  <symbol id="i-search" viewBox="0 0 16 16"><path d="M6.8 1.5a5.3 5.3 0 0 1 4.3 8.4l3.7 3.7-1.4 1.4-3.7-3.7A5.3 5.3 0 1 1 6.8 1.5zm0 2a3.3 3.3 0 1 0 0 6.6 3.3 3.3 0 0 0 0-6.6z"/></symbol>
  <symbol id="i-back" viewBox="0 0 16 16"><path d="M10.5 2.5 5 8l5.5 5.5 1.4-1.4L7.8 8l4.1-4.1z"/></symbol>
  <symbol id="i-go" viewBox="0 0 16 16"><path d="M8 1a7 7 0 1 1 0 14A7 7 0 0 1 8 1zm-.6 3.6L6.2 5.8 8.4 8l-2.2 2.2 1.2 1.2L10.8 8z"/></symbol>
  <symbol id="i-mark" viewBox="0 0 16 16"><path d="M3.5 1.5h9v13L8 11l-4.5 3.5z"/></symbol>
  <symbol id="i-menu" viewBox="0 0 16 16"><path d="M1.5 3h13v2h-13zm0 4h13v2h-13zm0 4h13v2h-13z"/></symbol>
  <symbol id="i-close" viewBox="0 0 16 16"><path d="M3.2 1.8 8 6.6l4.8-4.8 1.4 1.4L9.4 8l4.8 4.8-1.4 1.4L8 9.4l-4.8 4.8-1.4-1.4L6.6 8 1.8 3.2z"/></symbol>
</svg>

<!-- ================= Desktop: sidebar header ================= -->
<section class="screen desk" id="desk-overlay">
  <aside class="side">
    <div class="logo"><span class="back"><svg class="ic"><use href="#i-back"/></svg></span><span class="brand">Lumo</span></div>
    <ul class="nav">
      <li class="on"><svg class="ic"><use href="#i-home"/></svg>Home</li>
      <li><svg class="ic"><use href="#i-help"/></svg>How it works</li>
      <li><svg class="ic"><use href="#i-user"/></svg>About us</li>
      <li><svg class="ic"><use href="#i-trophy"/></svg>Leaderboard</li>
      <li><svg class="ic"><use href="#i-chat"/></svg>Weapons of comment</li>
    </ul>
  </aside>
  <div class="hero" role="img" aria-label="Concert crowd with raised hands in dim light"></div>
  <div class="tools">
    <span class="search">Search</span>
    <span class="round"><svg class="ic"><use href="#i-search"/></svg></span>
    <span class="btn login"><svg class="ic"><use href="#i-user"/></svg>Log in</span>
  </div>
  <main class="main">
    <section class="feed">
      <div class="feed-head"><h2>Foodies</h2><span class="btn sub"><svg class="ic"><use href="#i-mark"/></svg>Subscribe</span></div>
      <p class="intro">Nemo enim ipsam voluptatem quia voluptas sit aspernatur aut odit aut fugit sed quia consequuntur magni dolores eos qui ratione voluptatem sequi nesciunt neque porro quisquam.</p>
      <div class="grid">
        <article class="card"><div class="thumb t-pizza" role="img" aria-label="Pizza on a wooden board"><span class="len">12 Sec</span></div><h3>Nemo enim ipsam eeea voluptatem</h3><p class="meta"><span class="src"><i class="badge"></i>Foodies</span><time>3 days ago</time></p></article>
        <article class="card"><div class="thumb t-meat" role="img" aria-label="Grilled meat with herbs"><span class="len">1 min</span></div><h3>Duis aute irure dolor inre preheriderit</h3><p class="meta"><span class="src"><i class="badge"></i>Foodies</span><time>4 days ago</time></p></article>
        <article class="card"><div class="thumb t-steak" role="img" aria-label="Sliced steak with rosemary"><span class="len">5 min</span></div><h3>Ium dolore eu fugiat nulla pariatullum</h3><p class="meta"><span class="src"><i class="badge"></i>Foodies</span><time>3 days ago</time></p></article>
        <article class="card"><div class="thumb t-pasta" role="img" aria-label="Table of pasta dishes"><span class="len">20 Sec</span></div><h3>Sunt in culpaqui officia ea commodo</h3><p class="meta"><span class="src"><i class="badge"></i>Foodies</span><time>3 days ago</time></p></article>
      </div>
      <div class="load"><span class="btn">Load more <svg class="ic"><use href="#i-go"/></svg></span></div>
    </section>
    <section class="feed">
      <div class="feed-head"><h2>Healthy Living</h2><span class="btn sub"><svg class="ic"><use href="#i-mark"/></svg>Subscribe</span></div>
      <p class="intro">Nemo enim ipsam voluptatem quia voluptas sit aspernatur aut odit aut fugit sed quia consequuntur magni dolores eos qui ratione voluptatem sequi nesciunt neque porro quisquam.</p>
      <div class="grid">
        <article class="card"><div class="thumb t-sunset" role="img" aria-label="Person with raised arms at sunset"><span class="len">12 Sec</span></div><h3>Illum dolore eu fugiat nulla pariatu</h3><p class="meta"><span class="src"><i class="badge sq"></i>Healthy</span><time>3 days ago</time></p></article>
        <article class="card"><div class="thumb t-friends" role="img" aria-label="Two friends sharing fruit"><span class="len">1 min</span></div><h3>Duis aute irure dolor inre preheriderit</h3><p class="meta"><span class="src"><i class="badge sq"></i>Healthy</span><time>3 days ago</time></p></article>
        <article class="card"><div class="thumb t-bikes" role="img" aria-label="Couple cycling in a park"><span class="len">5 min</span></div><h3>Aute irurepre hdetsmo eiusmod tempor</h3><p class="meta"><span class="src"><i class="badge sq"></i>Healthy</span><time>3 days ago</time></p></article>
        <article class="card"><div class="thumb t-juice" role="img" aria-label="Woman holding a glass of juice"><span class="len">20 Sec</span></div><h3>Sunt in culpaqui officia ea commodo</h3><p class="meta"><span class="src"><i class="badge sq"></i>Healthy</span><time>4 days ago</time></p></article>
      </div>
      <div class="load"><span class="btn">Load more <svg class="ic"><use href="#i-go"/></svg></span></div>
    </section>
  </main>
  <footer class="foot"><span>TERMS OF SERVICE &nbsp;|&nbsp; PRIVACY &nbsp;|&nbsp; COPYRIGHT</span><span>Copyright © 2018 Lumo. All Rights Reserved.</span></footer>
</section>

<!-- ================= Desktop: top bar header ================= -->
<section class="screen desk" id="desk-bar">
  <header class="topbar">
    <div class="logo"><span class="back"><svg class="ic"><use href="#i-back"/></svg></span><span class="brand dark">Lumo</span></div>
    <div class="tools">
      <span class="search">Search</span>
      <span class="round"><svg class="ic"><use href="#i-search"/></svg></span>
      <span class="btn login"><svg class="ic"><use href="#i-user"/></svg>Log in</span>
    </div>
  </header>
  <aside class="side">
    <ul class="nav">
      <li class="on"><svg class="ic"><use href="#i-home"/></svg>Home</li>
      <li><svg class="ic"><use href="#i-help"/></svg>How it works</li>
      <li><svg class="ic"><use href="#i-user"/></svg>About us</li>
      <li><svg class="ic"><use href="#i-trophy"/></svg>Leaderboard</li>
      <li><svg class="ic"><use href="#i-chat"/></svg>Weapons of comment</li>
    </ul>
  </aside>
  <div class="hero" role="img" aria-label="Concert crowd with raised hands in dim light"></div>
  <main class="main">
    <section class="feed">
      <div class="feed-head"><h2>Foodies</h2><span class="btn sub"><svg class="ic"><use href="#i-mark"/></svg>Subscribe</span></div>
      <p class="intro">Nemo enim ipsam voluptatem quia voluptas sit aspernatur aut odit aut fugit sed quia consequuntur magni dolores eos qui ratione voluptatem sequi nesciunt neque porro quisquam.</p>
      <div class="grid">
        <article class="card"><div class="thumb t-pizza" role="img" aria-label="Pizza on a wooden board"><span class="len">12 Sec</span></div><h3>Nemo enim ipsam eeea voluptatem</h3><p class="meta"><span class="src"><i class="badge"></i>Foodies</span><time>3 days ago</time></p></article>
        <article class="card"><div class="thumb t-meat" role="img" aria-label="Grilled meat with herbs"><span class="len">1 min</span></div><h3>Duis aute irure dolor inre preheriderit</h3><p class="meta"><span class="src"><i class="badge"></i>Foodies</span><time>4 days ago</time></p></article>
        <article class="card"><div class="thumb t-steak" role="img" aria-label="Sliced steak with rosemary"><span class="len">5 min</span></div><h3>Ium dolore eu fugiat nulla pariatullum</h3><p class="meta"><span class="src"><i class="badge"></i>Foodies</span><time>3 days ago</time></p></article>
        <article class="card"><div class="thumb t-pasta" role="img" aria-label="Table of pasta dishes"><span class="len">20 Sec</span></div><h3>Sunt in culpaqui officia ea commodo</h3><p class="meta"><span class="src"><i class="badge"></i>Foodies</span><time>3 days ago</time></p></article>
      </div>
      <div class="load"><span class="btn">Load more <svg class="ic"><use href="#i-go"/></svg></span></div>
    </section>
    <section class="feed">
      <div class="feed-head"><h2>Healthy Living</h2><span class="btn sub"><svg class="ic"><use href="#i-mark"/></svg>Subscribe</span></div>
      <p class="intro">Nemo enim ipsam voluptatem quia voluptas sit aspernatur aut odit aut fugit sed quia consequuntur magni dolores eos qui ratione voluptatem sequi nesciunt neque porro quisquam.</p>
      <div class="grid">
        <article class="card"><div class="thumb t-sunset" role="img" aria-label="Person with raised arms at sunset"><span class="len">12 Sec</span></div><h3>Illum dolore eu fugiat nulla pariatu</h3><p class="meta"><span class="src"><i class="badge sq"></i>Healthy</span><time>3 days ago</time></p></article>
        <article class="card"><div class="thumb t-friends" role="img" aria-label="Two friends sharing fruit"><span class="len">1 min</span></div><h3>Duis aute irure dolor inre preheriderit</h3><p class="meta"><span class="src"><i class="badge sq"></i>Healthy</span><time>3 days ago</time></p></article>
        <article class="card"><div class="thumb t-bikes" role="img" aria-label="Couple cycling in a park"><span class="len">5 min</span></div><h3>Aute irurepre hdetsmo eiusmod tempor</h3><p class="meta"><span class="src"><i class="badge sq"></i>Healthy</span><time>3 days ago</time></p></article>
        <article class="card"><div class="thumb t-juice" role="img" aria-label="Woman holding a glass of juice"><span class="len">20 Sec</span></div><h3>Sunt in culpaqui officia ea commodo</h3><p class="meta"><span class="src"><i class="badge sq"></i>Healthy</span><time>4 days ago</time></p></article>
      </div>
      <div class="load"><span class="btn">Load more <svg class="ic"><use href="#i-go"/></svg></span></div>
    </section>
  </main>
  <footer class="foot"><span>TERMS OF SERVICE &nbsp;|&nbsp; PRIVACY &nbsp;|&nbsp; COPYRIGHT</span><span>Copyright © 2018 Lumo. All Rights Reserved.</span></footer>
</section>

<!-- ================= Mobile A: header over hero ================= -->
<section class="screen mob" id="mob-a">
  <div class="hero" role="img" aria-label="Concert crowd with raised hands in dim light"></div>
  <header class="bar"><span class="brand">Lumo</span><span class="acts"><span class="round"><svg class="ic"><use href="#i-search"/></svg></span><svg class="ic menu"><use href="#i-menu"/></svg></span></header>
  <main class="main">
    <section class="feed">
      <h2>Foodies</h2>
      <article class="card"><div class="thumb t-pizza" role="img" aria-label="Pizza on a wooden board"><span class="len">12 Sec</span></div><h3>Nemo enim ipsam eeeoluptatem</h3><p class="meta"><span class="src"><i class="badge"></i>Foodies</span><time>3 days ago</time></p></article>
      <article class="card"><div class="thumb t-meat" role="img" aria-label="Grilled meat with herbs"><span class="len">1 min</span></div><h3>Duis aute irure dolor preenderit</h3><p class="meta"><span class="src"><i class="badge"></i>Foodies</span><time>4 days ago</time></p></article>
      <article class="card"><div class="thumb t-steak" role="img" aria-label="Sliced steak with rosemary"><span class="len">5 min</span></div><h3>Ium dolore eu fugiat nulla tullum</h3><p class="meta"><span class="src"><i class="badge"></i>Foodies</span><time>3 days ago</time></p></article>
      <article class="card"><div class="thumb t-pasta" role="img" aria-label="Table of pasta dishes"><span class="len">20 Sec</span></div><h3>Sunt in culpaqui officia commodo</h3><p class="meta"><span class="src"><i class="badge"></i>Foodies</span><time>3 days ago</time></p></article>
      <div class="load"><span class="btn">Load more <svg class="ic"><use href="#i-go"/></svg></span></div>
    </section>
    <section class="feed">
      <h2>Healthy Living</h2>
      <article class="card"><div class="thumb t-friends" role="img" aria-label="Two friends sharing fruit"><span class="len">1 min</span></div><h3>Duis aute irure dolor inre preheriderit</h3><p class="meta"><span class="src"><i class="badge sq"></i>Healthy</span><time>3 days ago</time></p></article>
      <article class="card"><div class="thumb t-bikes" role="img" aria-label="Couple cycling in a park"><span class="len">5 min</span></div><h3>Aute irurepre hdetsmo eiusmod tempor</h3><p class="meta"><span class="src"><i class="badge sq"></i>Healthy</span><time>3 days ago</time></p></article>
      <article class="card"><div class="thumb t-sunset" role="img" aria-label="Person with raised arms at sunset"><span class="len">12 Sec</span></div><h3>Illum dolore eu fugiat nulla pariatu</h3><p class="meta"><span class="src"><i class="badge sq"></i>Healthy</span><time>3 days ago</time></p></article>
      <article class="card"><div class="thumb t-juice" role="img" aria-label="Woman holding a glass of juice"><span class="len">20 Sec</span></div><h3>Sunt in culpaqui officia ea commodo</h3><p class="meta"><span class="src"><i class="badge sq"></i>Healthy</span><time>4 days ago</time></p></article>
      <div class="load"><span class="btn">Load more <svg class="ic"><use href="#i-go"/></svg></span></div>
    </section>
  </main>
  <footer class="foot">TERMS OF SERVICE &nbsp;|&nbsp; PRIVACY &nbsp;|&nbsp; COPYRIGHT<br>Copyright © 2018 Lumo. All Rights Reserved.</footer>
</section>

<!-- ================= Mobile A: menu open ================= -->
<section class="screen mob" id="mob-a-menu">
  <div class="hero" role="img" aria-label="Concert crowd with raised hands in dim light"></div>
  <header class="bar"><span class="brand">Lumo</span><span class="acts"><span class="round"><svg class="ic"><use href="#i-search"/></svg></span><svg class="ic menu"><use href="#i-menu"/></svg></span></header>
  <main class="main">
    <section class="feed">
      <h2>Foodies</h2>
      <article class="card"><div class="thumb t-pizza" role="img" aria-label="Pizza on a wooden board"><span class="len">12 Sec</span></div><h3>Nemo enim ipsam eeeoluptatem</h3><p class="meta"><span class="src"><i class="badge"></i>Foodies</span><time>3 days ago</time></p></article>
      <article class="card"><div class="thumb t-meat" role="img" aria-label="Grilled meat with herbs"><span class="len">1 min</span></div><h3>Duis aute irure dolor preenderit</h3><p class="meta"><span class="src"><i class="badge"></i>Foodies</span><time>4 days ago</time></p></article>
      <article class="card"><div class="thumb t-steak" role="img" aria-label="Sliced steak with rosemary"><span class="len">5 min</span></div><h3>Ium dolore eu fugiat nulla tullum</h3><p class="meta"><span class="src"><i class="badge"></i>Foodies</span><time>3 days ago</time></p></article>
      <article class="card"><div class="thumb t-pasta" role="img" aria-label="Table of pasta dishes"><span class="len">20 Sec</span></div><h3>Sunt in culpaqui officia commodo</h3><p class="meta"><span class="src"><i class="badge"></i>Foodies</span><time>3 days ago</time></p></article>
      <div class="load"><span class="btn">Load more <svg class="ic"><use href="#i-go"/></svg></span></div>
    </section>
    <section class="feed">
      <h2>Healthy Living</h2>
      <article class="card"><div class="thumb t-friends" role="img" aria-label="Two friends sharing fruit"><span class="len">1 min</span></div><h3>Duis aute irure dolor inre preheriderit</h3><p class="meta"><span class="src"><i class="badge sq"></i>Healthy</span><time>3 days ago</time></p></article>
      <article class="card"><div class="thumb t-bikes" role="img" aria-label="Couple cycling in a park"><span class="len">5 min</span></div><h3>Aute irurepre hdetsmo eiusmod tempor</h3><p class="meta"><span class="src"><i class="badge sq"></i>Healthy</span><time>3 days ago</time></p></article>
      <article class="card"><div class="thumb t-sunset" role="img" aria-label="Person with raised arms at sunset"><span class="len">12 Sec</span></div><h3>Illum dolore eu fugiat nulla pariatu</h3><p class="meta"><span class="src"><i class="badge sq"></i>Healthy</span><time>3 days ago</time></p></article>
      <article class="card"><div class="thumb t-juice" role="img" aria-label="Woman holding a glass of juice"><span class="len">20 Sec</span></div><h3>Sunt in culpaqui officia ea commodo</h3><p class="meta"><span class="src"><i class="badge sq"></i>Healthy</span><time>4 days ago</time></p></article>
      <div class="load"><span class="btn">Load more <svg class="ic"><use href="#i-go"/></svg></span></div>
    </section>
  </main>
  <footer class="foot">TERMS OF SERVICE &nbsp;|&nbsp; PRIVACY &nbsp;|&nbsp; COPYRIGHT<br>Copyright © 2018 Lumo. All Rights Reserved.</footer>
  <div class="veil"></div>
  <svg class="ic close"><use href="#i-close"/></svg>
  <nav class="drawer">
    <ul class="nav">
      <li class="on"><svg class="ic"><use href="#i-home"/></svg>Home</li>
      <li><svg class="ic"><use href="#i-help"/></svg>How it works</li>
      <li><svg class="ic"><use href="#i-user"/></svg>About us</li>
      <li><svg class="ic"><use href="#i-trophy"/></svg>Leaderboard</li>
      <li><svg class="ic"><use href="#i-chat"/></svg>Weapons of comment</li>
    </ul>
  </nav>
</section>

<!-- ================= Mobile B: white top bar ================= -->
<section class="screen mob lite" id="mob-b">
  <div class="hero" role="img" aria-label="Concert crowd with raised hands in dim light"></div>
  <header class="bar"><span class="brand dark">Lumo</span><span class="acts"><span class="round"><svg class="ic"><use href="#i-search"/></svg></span><svg class="ic menu"><use href="#i-menu"/></svg></span></header>
  <main class="main">
    <section class="feed">
      <h2>Foodies</h2>
      <article class="card"><div class="thumb t-pizza" role="img" aria-label="Pizza on a wooden board"><span class="len">12 Sec</span></div><h3>Nemo enim ipsam eeeoluptatem</h3><p class="meta"><span class="src"><i class="badge"></i>Foodies</span><time>3 days ago</time></p></article>
      <article class="card"><div class="thumb t-meat" role="img" aria-label="Grilled meat with herbs"><span class="len">1 min</span></div><h3>Duis aute irure dolor preenderit</h3><p class="meta"><span class="src"><i class="badge"></i>Foodies</span><time>4 days ago</time></p></article>
      <article class="card"><div class="thumb t-steak" role="img" aria-label="Sliced steak with rosemary"><span class="len">5 min</span></div><h3>Ium dolore eu fugiat nulla tullum</h3><p class="meta"><span class="src"><i class="badge"></i>Foodies</span><time>3 days ago</time></p></article>
      <article class="card"><div class="thumb t-pasta" role="img" aria-label="Table of pasta dishes"><span class="len">20 Sec</span></div><h3>Sunt in culpaqui officia commodo</h3><p class="meta"><span class="src"><i class="badge"></i>Foodies</span><time>3 days ago</time></p></article>
      <div class="load"><span class="btn">Load more <svg class="ic"><use href="#i-go"/></svg></span></div>
    </section>
    <section class="feed">
      <h2>Healthy Living</h2>
      <article class="card"><div class="thumb t-friends" role="img" aria-label="Two friends sharing fruit"><span class="len">1 min</span></div><h3>Duis aute irure dolor inre preheriderit</h3><p class="meta"><span class="src"><i class="badge sq"></i>Healthy</span><time>3 days ago</time></p></article>
      <article class="card"><div class="thumb t-bikes" role="img" aria-label="Couple cycling in a park"><span class="len">5 min</span></div><h3>Aute irurepre hdetsmo eiusmod tempor</h3><p class="meta"><span class="src"><i class="badge sq"></i>Healthy</span><time>3 days ago</time></p></article>
      <article class="card"><div class="thumb t-sunset" role="img" aria-label="Person with raised arms at sunset"><span class="len">12 Sec</span></div><h3>Illum dolore eu fugiat nulla pariatu</h3><p class="meta"><span class="src"><i class="badge sq"></i>Healthy</span><time>3 days ago</time></p></article>
      <article class="card"><div class="thumb t-juice" role="img" aria-label="Woman holding a glass of juice"><span class="len">20 Sec</span></div><h3>Sunt in culpaqui officia ea commodo</h3><p class="meta"><span class="src"><i class="badge sq"></i>Healthy</span><time>4 days ago</time></p></article>
      <div class="load"><span class="btn">Load more <svg class="ic"><use href="#i-go"/></svg></span></div>
    </section>
  </main>
  <footer class="foot">TERMS OF SERVICE &nbsp;|&nbsp; PRIVACY &nbsp;|&nbsp; COPYRIGHT<br>Copyright © 2018 Lumo. All Rights Reserved.</footer>
</section>

<!-- ================= Mobile B: menu open ================= -->
<section class="screen mob lite" id="mob-b-menu">
  <div class="hero" role="img" aria-label="Concert crowd with raised hands in dim light"></div>
  <header class="bar"><span class="brand dark">Lumo</span><span class="acts"><span class="round"><svg class="ic"><use href="#i-search"/></svg></span><svg class="ic menu"><use href="#i-menu"/></svg></span></header>
  <main class="main">
    <section class="feed">
      <h2>Foodies</h2>
      <article class="card"><div class="thumb t-pizza" role="img" aria-label="Pizza on a wooden board"><span class="len">12 Sec</span></div><h3>Nemo enim ipsam eeeoluptatem</h3><p class="meta"><span class="src"><i class="badge"></i>Foodies</span><time>3 days ago</time></p></article>
      <article class="card"><div class="thumb t-meat" role="img" aria-label="Grilled meat with herbs"><span class="len">1 min</span></div><h3>Duis aute irure dolor preenderit</h3><p class="meta"><span class="src"><i class="badge"></i>Foodies</span><time>4 days ago</time></p></article>
      <article class="card"><div class="thumb t-steak" role="img" aria-label="Sliced steak with rosemary"><span class="len">5 min</span></div><h3>Ium dolore eu fugiat nulla tullum</h3><p class="meta"><span class="src"><i class="badge"></i>Foodies</span><time>3 days ago</time></p></article>
      <article class="card"><div class="thumb t-pasta" role="img" aria-label="Table of pasta dishes"><span class="len">20 Sec</span></div><h3>Sunt in culpaqui officia commodo</h3><p class="meta"><span class="src"><i class="badge"></i>Foodies</span><time>3 days ago</time></p></article>
      <div class="load"><span class="btn">Load more <svg class="ic"><use href="#i-go"/></svg></span></div>
    </section>
    <section class="feed">
      <h2>Healthy Living</h2>
      <article class="card"><div class="thumb t-friends" role="img" aria-label="Two friends sharing fruit"><span class="len">1 min</span></div><h3>Duis aute irure dolor inre preheriderit</h3><p class="meta"><span class="src"><i class="badge sq"></i>Healthy</span><time>3 days ago</time></p></article>
      <article class="card"><div class="thumb t-bikes" role="img" aria-label="Couple cycling in a park"><span class="len">5 min</span></div><h3>Aute irurepre hdetsmo eiusmod tempor</h3><p class="meta"><span class="src"><i class="badge sq"></i>Healthy</span><time>3 days ago</time></p></article>
      <article class="card"><div class="thumb t-sunset" role="img" aria-label="Person with raised arms at sunset"><span class="len">12 Sec</span></div><h3>Illum dolore eu fugiat nulla pariatu</h3><p class="meta"><span class="src"><i class="badge sq"></i>Healthy</span><time>3 days ago</time></p></article>
      <article class="card"><div class="thumb t-juice" role="img" aria-label="Woman holding a glass of juice"><span class="len">20 Sec</span></div><h3>Sunt in culpaqui officia ea commodo</h3><p class="meta"><span class="src"><i class="badge sq"></i>Healthy</span><time>4 days ago</time></p></article>
      <div class="load"><span class="btn">Load more <svg class="ic"><use href="#i-go"/></svg></span></div>
    </section>
  </main>
  <footer class="foot">TERMS OF SERVICE &nbsp;|&nbsp; PRIVACY &nbsp;|&nbsp; COPYRIGHT<br>Copyright © 2018 Lumo. All Rights Reserved.</footer>
  <div class="veil"></div>
  <svg class="ic close"><use href="#i-close"/></svg>
  <nav class="drawer">
    <ul class="nav">
      <li class="on"><svg class="ic"><use href="#i-home"/></svg>Home</li>
      <li><svg class="ic"><use href="#i-help"/></svg>How it works</li>
      <li><svg class="ic"><use href="#i-user"/></svg>About us</li>
      <li><svg class="ic"><use href="#i-trophy"/></svg>Leaderboard</li>
      <li><svg class="ic"><use href="#i-chat"/></svg>Weapons of comment</li>
    </ul>
  </nav>
</section>

</body>
</html>
```